Commercial Real Estate Executive Recruiting Firm Needs Business Card Design

We need a business card design for MARLOW | Executive Recruiting - an executive recruiting firm focused exclusively on the commercial real estate industry. We place professionals ranging from Analyst to the Executive Office covering all investment/finance disciplines (acquisitions, asset management, capital markets, etc.) in all product types (office, retail, multifamily, industrial, land, etc.). We have a passion for helping people (clients and candidates) and have a reputation for being open and honest in our recruiting - and yes, very successful. We have recently developed a new logo and would like to update our business cards as well. I've uploaded some information about our company that contains the new logo.

Target Market(s)

Commercial Real Estate professionals. Primarily in the US. These are typically, smart, driven professionals with finance degrees and MBAs. Primarily men between the ages of 25 and 55.

Industry/Entity Type

Real Estate

Font styles to use
Other font styles liked:
• The font for "MARLOW" is Blair ITC (Medium), and "executive recruiting" is Gotham (Book).

Requirements
Must have
• I like the idea of white background on one side and solid color (blue, black, etc.) on back of card.

Would like to utilize the fonts in the logo (to the extent possible) so as to not have too many fonts on card.
Nice to have
• I think the roles (i.e., Acquisitions, Asset Management, etc.,...) is probably likely best placed on the back side of the card with the logo maybe. See attached current business card for content.

```html
<!DOCTYPE html>
<html lang="en">
<head>
<meta charset="utf-8">
<title>MARLOW | Executive Recruiting — Business Card</title>
<link rel="stylesheet" href="https://fonts.googleapis.com/css2?family=Montserrat:wght@400;500;600&display=swap">
<style>
  :root {
    --brand-blue: #3b86c8;
    --band-blue: #3d87cc;
    --ink-dark: #2b2b2b;
    --ink-grey: #555a60;
    --rule-dark: #1f2a36;
    --card-white: #ffffff;
    --stage: #eef0f2;
  }
  * { box-sizing: border-box; margin: 0; padding: 0; }
  html, body {
    width: 1200px; height: 720px; overflow: hidden;
    background: var(--stage);
    font-family: "Montserrat", Arial, sans-serif;
  }
  .canvas { position: relative; width: 1200px; height: 720px; }

  .card {
    position: absolute; width: 540px; height: 309px;
    box-shadow: 0 6px 18px rgba(0,0,0,0.18);
    overflow: hidden;
  }

  /* Front */
  .card-front { left: 40px; top: 90px; background: var(--card-white); }
  .brand-lockup {
    position: absolute; left: 100px; top: 36px;
    display: flex; align-items: center; gap: 14px;
    white-space: nowrap;
  }
  .brand-square { width: 40px; height: 40px; background: var(--brand-blue); flex: none; }
  .brand-text {
    display: flex; flex-direction: column;
    color: var(--ink-dark); font-weight: 400;
    border-left: 1px solid #b9bdc2; padding-left: 12px;
  }
  .brand-name { font-size: 30px; letter-spacing: 9px; line-height: 32px; }
  .brand-tagline { font-size: 13px; letter-spacing: 3.4px; line-height: 16px; }

  .name-band {
    position: absolute; left: 0; right: 0; top: 112px; height: 28px;
    background: var(--band-blue);
    border-top: 2px solid var(--rule-dark);
    color: #fff; font-size: 15px; font-weight: 600;
    display: flex; align-items: center; justify-content: center;
    padding-left: 40px;
  }
  .name-band .title { font-weight: 400; }
  .divider {
    position: absolute; left: 238px; top: 146px; width: 1px; height: 116px;
    background: #c9ccd0;
  }
  .contact-list {
    position: absolute; left: 250px; top: 150px; list-style: none;
    font-size: 12.5px; color: var(--ink-grey);
  }
  .contact-list li { display: flex; align-items: center; gap: 7px; height: 20px; }
  .contact-icon { width: 13px; height: 13px; flex: none; }
  .lower-band {
    position: absolute; left: 0; right: 0; top: 216px; height: 18px;
    background: var(--band-blue);
    border-top: 2px solid var(--rule-dark);
  }
  .address {
    position: absolute; right: 316px; top: 240px; text-align: right;
    font-style: normal; font-size: 12.5px; line-height: 18px; color: var(--ink-grey);
    white-space: nowrap;
  }

  /* Back */
  .card-back { left: 620px; top: 320px; background: var(--brand-blue); color: #fff; }
  .back-brand {
    position: absolute; right: 34px; top: 32px;
    display: flex; align-items: center; gap: 10px;
  }
  .back-brand .brand-square { background: #fff; width: 34px; height: 34px; }
  .back-brand .brand-name { color: #fff; font-size: 22px; letter-spacing: 4px; }
  .mission {
    position: absolute; left: 30px; top: 92px; width: 300px;
    font-size: 12.5px; line-height: 17px;
  }
  .strengths {
    position: absolute; left: 30px; top: 160px; list-style: none;
    font-size: 13.5px; line-height: 26px;
  }
  .strengths li::before {
    content: ""; display: inline-block; width: 6px; height: 6px;
    border-radius: 50%; background: #fff; margin-right: 9px; vertical-align: middle;
  }
</style>
</head>
<body>
<main class="canvas">

  <section class="card card-front" aria-label="Business card front">
    <div class="brand-lockup">
      <span class="brand-square"></span>
      <span class="brand-text">
        <span class="brand-name">MARLOW</span>
        <span class="brand-tagline">executive recruiting</span>
      </span>
    </div>
    <div class="name-band">Your Name,&nbsp;<span class="title">Title</span></div>
    <div class="divider"></div>
    <ul class="contact-list">
      <li>
        <svg class="contact-icon" viewBox="0 0 14 14" aria-hidden="true">
          <circle cx="7" cy="7" r="7" fill="var(--brand-blue)"/>
          <path d="M4.5 3.5l1.6 0 .6 2-1 .8a5 5 0 0 0 2.4 2.4l.8-1 2 .6v1.6c-3.8.4-6.8-2.6-6.4-6.4z" fill="#fff"/>
        </svg>214-555-0148
      </li>
      <li>
        <svg class="contact-icon" viewBox="0 0 14 14" aria-hidden="true">
          <circle cx="7" cy="7" r="7" fill="var(--brand-blue)"/>
          <rect x="3.5" y="4.5" width="7" height="5" fill="#fff"/>
          <path d="M3.5 4.5L7 7.3l3.5-2.8" stroke="var(--brand-blue)" stroke-width="0.8" fill="none"/>
        </svg>sam@marlowrecruiting.com
      </li>
      <li>
        <svg class="contact-icon" viewBox="0 0 14 14" aria-hidden="true">
          <circle cx="7" cy="7" r="7" fill="var(--brand-blue)"/>
          <circle cx="7" cy="7" r="3.6" fill="none" stroke="#fff" stroke-width="0.9"/>
          <path d="M3.4 7h7.2M7 3.4c-1.6 2-1.6 5.2 0 7.2M7 3.4c1.6 2 1.6 5.2 0 7.2" stroke="#fff" stroke-width="0.7" fill="none"/>
        </svg>www.marlowrecruiting.com
      </li>
    </ul>
    <div class="lower-band"></div>
    <address class="address">
      <div>1450 Larkspur Lane</div>
      <div>Fairview, Texas 75024</div>
    </address>
  </section>

  <section class="card card-back" aria-label="Business card back">
    <div class="back-brand">
      <span class="brand-square"></span>
      <span class="brand-name">MARLOW</span>
    </div>
    <p class="mission">We are trusted advisors who partner with our clients offer focused representation develop organizations, and get results</p>
    <ul class="strengths">
      <li>Industry Experience &amp; Track Record</li>
      <li>Industry Involvement &amp; Leadership</li>
      <li>Complete Confidentiality &amp; Communication</li>
      <li>Post Placement Follow Up &amp; Support</li>
      <li>A Commitment To Research &amp; Referral Based Recruiting</li>
    </ul>
  </section>

</main>
</body>
</html>
```